Velmora Investments - stationery for luxury, exclusive property investment company

We need stationery (letterhead, folder, compliments slip and envelope) and business cards which will reflect our luxury brand.

I have attached some design examples that we like.

We are an investment company which buys property to provide accommodation for corporate customers.

The design of the stationery needs to be be simple, refined, understated, luxury and very tasteful.

The design should communicate luxury and exclusivity, without being ostentatious.

Logo files are attached
Updates

Please can designers re-read the brief, and make sure the logo is in gold on either on a navy or white background.

Target Market(s)

Wealthy customers

Contact Information for Business Card

Laura Penhaligon-Ward
Director
Velmora Investments Limited
email: laura@velmorainvestments-example.co.uk
mob: 07700900412

Font styles to use
Serif

Colors

Designer to choose colors to be used in the design.

Requirements
Must have
• The logo must be gold on either a white or navy background as per the attached logos.
• The stationery MUST have the following information:
• Velmora Investments Limited
• The Larches
• Wexley Rise
• Ashcombe
• ZX19 2QP
• Company Number: 48273615 (Registered in England and Wales)
• The letterhead must also have the two attached logos for the KPV and the KPV accreditation scheme. They do not need to be large.
Nice to have
• A watermark, navy banding either top or bottom.
Should not have
• Anything that looks budget.

```html
<!DOCTYPE html>
<html lang="en">
<head>
<meta charset="utf-8">
<title>Velmora Investments – Stationery</title>
<link rel="stylesheet" href="https://fonts.googleapis.com/css2?family=Cormorant+Garamond:wght@500&family=Tinos:wght@400;700&family=Lato:wght@400;700&display=swap">
<style>
:root{
  --backdrop:#4a4a4c;
  --paper:#eeeeee;
  --navy:#0e1433;
  --gold:#b8933f;
  --gold-light:#e2cf8c;
  --gold-dark:#9a7a30;
  --ink:#333;
  --ink-soft:#5a5a5a;
  --badge-red:#d8392f;
}
*{margin:0;padding:0;box-sizing:border-box}
html,body{width:1200px;height:760px;overflow:hidden;background:var(--backdrop)}
.canvas{position:relative;width:1200px;height:760px}
.sheet{position:absolute;background:var(--paper);box-shadow:0 3px 10px rgba(0,0,0,.35)}
.gold-rule{position:absolute;left:0;right:0;bottom:0;height:5px;background:linear-gradient(90deg,var(--gold-dark),var(--gold-light),var(--gold),var(--gold-light),var(--gold-dark))}

.brand{font-family:"Cormorant Garamond",serif;font-weight:500;color:var(--gold);text-align:center;line-height:1.05;letter-spacing:.08em;text-transform:uppercase}
.brand .dot{display:block;margin:0 auto 5px;border-radius:50%;border:1.5px solid var(--gold)}
.brand .sub{display:block;letter-spacing:.32em}

.serif{font-family:"Tinos",serif}

.card-navy{left:124px;top:56px;width:218px;height:122px;background:var(--navy)}
.card-navy .brand{position:absolute;left:0;right:0;top:26px;font-size:14px}
.card-navy .brand .dot{width:18px;height:18px}
.card-navy .brand .sub{font-size:8px;margin-top:2px}
.card-navy .reg{position:absolute;left:0;right:0;bottom:12px;text-align:center;font-size:5px;color:var(--gold);letter-spacing:.05em}

.card-white{left:370px;top:56px;width:216px;height:122px}
.card-white .brand{position:absolute;left:0;right:0;top:12px;font-size:9.5px}
.card-white .brand .dot{width:12px;height:12px;margin-bottom:3px}
.card-white .brand .sub{font-size:5.5px;margin-top:1px}
.card-white .person{position:absolute;left:0;right:0;top:64px;text-align:center;color:var(--gold);font-size:6.5px;font-weight:700;letter-spacing:.04em;text-transform:uppercase}
.card-white .role{position:absolute;left:0;right:0;top:73px;text-align:center;color:var(--ink-soft);font-size:4.5px}
.card-white .contacts{position:absolute;left:0;right:0;top:94px;text-align:center;color:var(--ink);font-size:4.6px;line-height:1.35}
.card-white .gold-rule{height:3px}

.icon-row{position:absolute;display:flex;align-items:center;gap:2px}
.icon-row .line{height:1px;background:var(--gold)}
.icon-row svg{display:block}

.env-front{left:38px;top:210px;width:548px;height:236px}
.env-front .brand{position:absolute;right:38px;top:22px;font-size:17px}
.env-front .brand .dot{width:22px;height:22px}
.env-front .brand .sub{font-size:9.5px;margin-top:2px}
.env-front .reg{position:absolute;left:28px;top:163px;font-size:8px;color:#222}
.env-front .tick{position:absolute;left:28px;top:180px;width:16px;height:1.5px;background:var(--gold)}
.env-front .addr{position:absolute;left:28px;top:187px;font-size:7.6px;line-height:1.2;color:#333}

.env-back{left:38px;top:475px;width:548px;height:237px;background:#ececec}
.env-back svg.flap{position:absolute;left:0;top:0}
.env-back .flap-name{position:absolute;left:0;right:0;top:30px;font-size:12px;color:#f1e6bf}
.env-back .return{position:absolute;left:0;right:0;bottom:22px;text-align:center;font-size:7.4px;line-height:1.25;color:#333}

.letter{left:629px;top:38px;width:523px;height:674px;
  background:linear-gradient(180deg,#e6e6e6 0,#ececec 225px,#efefef 226px,#f1f1f1 452px,#e9e9e9 453px,#f0f0f0 674px)}
.letter .brand{position:absolute;left:25px;top:30px;width:135px;font-size:14px}
.letter .brand .dot{width:22px;height:22px}
.letter .brand .sub{font-size:8px;margin-top:2px}
.badges{position:absolute;left:377px;top:39px;display:flex;gap:8px}
.badges span{display:block;height:18px;background:var(--badge-red);border-radius:1px}
.badges .b1{width:46px;background:linear-gradient(180deg,var(--badge-red) 55%,#e9775a 55%)}
.badges .b2{width:39px}
.letter .reg{position:absolute;left:377px;top:62px;font-size:7.6px;color:#333}
.letter-body{position:absolute;left:55px;width:412px;font-family:"Lato",sans-serif;color:var(--ink-soft);font-size:8.1px;line-height:11.2px}
.date{top:146px}
.recipient{top:168px}
.recipient b{color:#444;font-weight:700}
.salutation{top:236px}
.para{text-align:justify}
.p1{top:258px}.p2{top:348px}.p3{top:415px}
.closing{top:470px}
.signature{position:absolute;left:50px;top:483px;width:235px;height:22px;background:linear-gradient(90deg,rgba(40,40,40,.12),rgba(40,40,40,.05));border-radius:2px}
.signoff{top:508px}
.signoff b{color:#444;font-weight:700}
.letter .icon-row{left:115px;top:619px}
.letter-footer{position:absolute;left:0;right:0;top:632px;text-align:center;font-size:7.6px;line-height:9.8px;color:#333}
</style>
</head>
<body>
<div class="canvas">

  <section class="sheet card-navy serif">
    <div class="brand"><span class="dot"></span>Velmora<span class="sub">Investments</span></div>
    <p class="reg">COMPANY NUMBER : 48273615</p>
  </section>

  <section class="sheet card-white serif">
    <div class="brand"><span class="dot"></span>Velmora<span class="sub">Investments</span></div>
    <p class="person">Laura Penhaligon-Ward</p>
    <p class="role">Director</p>
    <div class="icon-row" style="left:28px;top:84px">
      <span class="line" style="width:62px"></span>
      <svg width="34" height="6" viewBox="0 0 34 6"><g fill="var(--gold)"><circle cx="3" cy="3" r="2.6"/><circle cx="10" cy="3" r="2.6"/><circle cx="17" cy="3" r="2.6"/><circle cx="24" cy="3" r="2.6"/><circle cx="31" cy="3" r="2.6"/></g></svg>
      <span class="line" style="width:62px"></span>
    </div>
    <p class="contacts">020.7946.0811 &nbsp;|&nbsp; 07700900412<br>laura@velmorainvestments-example.co.uk<br>Velmora Investments Limited, The Larches, Wexley Rise, Ashcombe, ZX19 2QP</p>
    <span class="gold-rule"></span>
  </section>

  <section class="sheet env-front serif">
    <div class="brand"><span class="dot"></span>Velmora<span class="sub">Investments</span></div>
    <p class="reg">Company Number: 48273615</p>
    <span class="tick"></span>
    <p class="addr">Velmora Investments Limited<br>The Larches, Wexley Rise<br>Ashcombe, ZX19 2QP</p>
    <span class="gold-rule"></span>
  </section>

  <section class="sheet env-back serif">
    <svg class="flap" width="548" height="100" viewBox="0 0 548 100">
      <defs>
        <linearGradient id="flapGold" x1="0" y1="0" x2="1" y2="0">
          <stop offset="0" stop-color="#9a7a30"/>
          <stop offset=".45" stop-color="#d9c27a"/>
          <stop offset=".7" stop-color="#c6a552"/>
          <stop offset="1" stop-color="#a7863a"/>
        </linearGradient>
      </defs>
      <path d="M0 0 H548 L532 75 Q529 80 522 80 H26 Q19 80 16 75 Z" fill="url(#flapGold)"/>
      <path d="M16 80 L10 100 M532 80 L538 100" stroke="#d6d6d6" stroke-width="1" fill="none"/>
    </svg>
    <div class="brand flap-name">Velmora</div>
    <p class="return"><b>If undelivered, please return to:</b><br>Velmora Investments Limited, The Larches, Wexley Rise, Ashcombe, ZX19 2QP</p>
  </section>

  <section class="sheet letter">
    <div class="brand serif"><span class="dot"></span>Velmora<span class="sub">Investments</span></div>
    <div class="badges" role="img" aria-label="KPV membership and KPV accreditation scheme badges"><span class="b1"></span><span class="b2"></span></div>
    <p class="reg serif">Company Number : 48273615</p>

    <p class="letter-body date">January 1, 2050</p>
    <p class="letter-body recipient"><b>Daniel Hartley</b><br>Managing Director<br>Co.Street, Building/Suite<br>City/State, Zip Code</p>
    <p class="letter-body salutation">Dear Oliver Brenton,</p>
    <p class="letter-body para p1">Lorem ipsum dolor sit amet, consectetuer adipiscing elit, sed diam nonummy nibh euismod tincidunt ut laoreet dolore magna aliquam erat volutpat. Ut wisi enim ad minim veniam, quis nostrud exerci tation ullamcorper suscipit lobortis nisl ut aliquip ex ea commodo consequat. Duis dolore te feugait nulla facilisi. Nam liber tempor cum soluta nobis eleifend option congue nihil imperdiet doming id quod mazim placerat facer possim assum. Lorem ipsum dolor sit amet, consectetuer adipiscing elit, sed diam nonummy nibh euismod tincidunt ut laoreet dolore magna aliquam erat volutpat. Ut wisi enim ad minim veniam, quis nostrud exerci tation ullamcorper suscipit lobortis nisl ut aliquip ex ea commodo consequat.</p>
    <p class="letter-body para p2">Consectetuer adipiscing elit, sed diam nonummy nibh euismod tincidunt ut laoreet dolore magna aliquam erat volutpat. Ut wisi enim ad minim veniam, quis nostrud exerci tation ullamcorper suscipit lobortis nisl ut aliquip ex ea commodo consequat. Consectetuer adipiscing elit, sed diam nonummy nibh euismod tincidunt ut laoreet dolore magna aliquam erat volutpat. Ut wisi enim ad minim veniam, quis nostrud exerci tation ullamcorper suscipit lobortis nisl ut aliquip ex ea commodo consequat.</p>
    <p class="letter-body para p3">Duis dolore te feugait nulla facilisi. Nam liber tempor cum soluta nobis eleifend option congue nihil imperdiet doming id quod mazim placerat facer possim assum. Duis dolore te feugait nulla facilisi. Nam liber tempor cum soluta nobis eleifend option congue nihil imperdiet doming id quod mazim placerat facer possim assum.</p>
    <p class="letter-body closing">Sincerely Yours,</p>
    <div class="signature" role="img" aria-label="Handwritten signature of the managing director"></div>
    <p class="letter-body signoff"><b>Authorized Managing Director</b><br>Company Name Here</p>

    <div class="icon-row">
      <span class="line" style="width:118px"></span>
      <svg width="58" height="9" viewBox="0 0 58 9"><g fill="var(--gold)"><circle cx="4.5" cy="4.5" r="4"/><circle cx="16.5" cy="4.5" r="4"/><circle cx="28.5" cy="4.5" r="4"/><circle cx="40.5" cy="4.5" r="4"/><circle cx="52.5" cy="4.5" r="4"/></g><g fill="#fff"><path d="M3 2.6h1l.5 1.2-.6.5a3 3 0 0 0 1.3 1.3l.5-.6 1.2.5v1A.6.6 0 0 1 6.3 7 4.2 4.2 0 0 1 2.4 3.1.6.6 0 0 1 3 2.6z"/><rect x="14.4" y="3" width="4.2" height="3" rx=".4"/><rect x="26.4" y="3" width="4.2" height="3" rx=".4"/><circle cx="40.5" cy="4.5" r="2" fill="none" stroke="#fff" stroke-width=".8"/><path d="M52.5 2a1.8 1.8 0 0 1 1.8 1.8c0 1.3-1.8 3.2-1.8 3.2s-1.8-1.9-1.8-3.2A1.8 1.8 0 0 1 52.5 2z"/></g></svg>
      <span class="line" style="width:118px"></span>
    </div>
    <p class="letter-footer serif">020.7946.0811 &nbsp;|&nbsp; 020.7946.0922<br>info@velmorainvestments-example.co.uk &nbsp;|&nbsp; www.velmorainvestments-example.co.uk<br>Velmora Investments Limited, The Larches, Wexley Rise, Ashcombe, ZX19 2QP</p>
    <span class="gold-rule"></span>
  </section>

</div>
</body>
</html>
```